Navelo Partnering Business Card

Hello everyone. We need a business card design that would match our logo and the theme we're trying to have for Navelo that you can find on our website and/or Corvapage page

```html
<!DOCTYPE html>
<html lang="en">
<head>
<meta charset="UTF-8">
<title>Navelo Business Card</title>
<link rel="stylesheet" href="https://fonts.googleapis.com/css2?family=Montserrat:wght@400;500;700&display=swap">
<style>
  :root {
    --backdrop: #a9b8be;
    --card-purple: #3c2b60;
    --card-edge: #2a1d45;
    --ink-light: #ece9f2;
    --ink-soft: #cfc8de;
  }
  * { margin: 0; padding: 0; box-sizing: border-box; }
  html, body {
    width: 1200px; height: 969px; overflow: hidden;
    background: var(--backdrop);
    font-family: "Montserrat", sans-serif;
  }
  .sheet {
    width: 1200px; height: 969px;
    display: flex; flex-direction: column; align-items: center; justify-content: center;
    gap: 56px;
  }
  .card {
    position: relative;
    width: 640px; height: 366px;
    background: var(--card-purple);
    border-bottom: 3px solid var(--card-edge);
    color: var(--ink-light);
  }
  .card-front { display: flex; align-items: center; justify-content: center; }
  .brand-mark { display: flex; align-items: center; gap: 18px; }
  .brand-dot {
    width: 22px; height: 22px; border-radius: 50%;
    background: var(--ink-light);
  }
  .brand-name { font-weight: 700; color: var(--ink-light); letter-spacing: 1px; }
  .card-front .brand-name { font-size: 72px; }
  .card-back .brand-mark { position: absolute; right: 48px; bottom: 56px; gap: 9px; }
  .card-back .brand-dot { width: 10px; height: 10px; }
  .card-back .brand-name { font-size: 30px; }

  .holder { position: absolute; left: 52px; top: 50px; }
  .holder-name { font-size: 24px; font-weight: 700; }
  .holder-title { font-size: 13px; font-weight: 500; color: var(--ink-soft); margin-top: 2px; }
  .address { position: absolute; left: 52px; top: 138px; font-size: 14px; line-height: 1.45; }
  .website { position: absolute; left: 52px; top: 210px; font-size: 14px; }
  .website strong { font-weight: 700; }
  .contacts { position: absolute; left: 230px; top: 250px; font-size: 14px; line-height: 1.35; }
  .contact-label { font-weight: 700; font-size: 13px; }
  .contact-value { margin-bottom: 8px; }
</style>
</head>
<body>
<main class="sheet">
  <section class="card card-front">
    <div class="brand-mark">
      <span class="brand-dot"></span>
      <span class="brand-name">Navelo</span>
    </div>
  </section>

  <section class="card card-back">
    <div class="holder">
      <p class="holder-name">Daniel Reyes</p>
      <p class="holder-title">Managing Director</p>
    </div>
    <p class="address">118 Harbor Ln 12<br>Fairview, CA 90210</p>
    <p class="website">www.<strong>navelo-example</strong>.com</p>
    <div class="contacts">
      <p class="contact-label">mobile</p>
      <p class="contact-value">555.010.2040</p>
      <p class="contact-label">email</p>
      <p class="contact-value">hi@navelo-example.com</p>
    </div>
    <div class="brand-mark">
      <span class="brand-dot"></span>
      <span class="brand-name">Navelo</span>
    </div>
  </section>
</main>
</body>
</html>
```